App user experience screen shot design

Hi guys – this is a two part competition. This competition is to design one (1) corporate phone app screenshot as a demonstration of your skill and interpretation of the proposal.

However, I need 35 app screenshots designed – this is design only, not the app build. The screenshots are for a corporate (real estate industry) app that will be built in coming months – this part of the project is to visually demonstrate user experience. All 35 screenshots are text based but may use icons or visual aids to improve user experience.

For this competition – to assess your design skills I’d like you to design a “register” page with:
1. Name
2. Email
3. Password
4. Phone
5. Birth date
6. Address
7. Accept terms/conditions
Obviously there is very little room for creativity when designing a register page - but this is deliberate, only truly excellent graphic designers can make a boring register page awesome.

The app company logo is attached and you can go to their website to get an idea of the design intention. The font used in the logo is Gatham Bold, you’ll be able to find it and download for free online if you don’t already have it.

In your submission – in the lower right hand corner of your design please indicate bid for the 35 screenshots with your cost ($) and the time it will take you to deliver – so “35 screenshots for $xxx in X days”. Any submissions without this will be automatically rejected.

Any questions – feel free to get in contact! Good luck.

The competition will be unsealed for 2 days to encourage broader collaboration and then sealed to avoid plagiarism for the remaining time the competition runs for. If standout work is identified early in the completion I reserve the right to close the competition and award early.

<<<UPDATE>>>
Hi guys - as discussed, I've now sealed the comp.

As a little feedback for all to consider, I prefer registration pages that are modern and corporate. I don't like curved edges to data cells - I prefer square or bevelled corners. Colors need to be corporate but inviting and I prefer registration pages with "selfies" or profile image uploaders.

Don't forget that all submissions must include a tender for the 35 screenshots - and preference will be given to high quality work where you have access to coders who can potentially build the app and you recommend as having skill and attention to detail equal to your own.

Good luck!

```html
<!DOCTYPE html>
<html lang="en">
<head>
<meta charset="utf-8">
<title>Keystead – Register screen</title>
<link href="https://fonts.googleapis.com/css2?family=Montserrat:wght@300;400;500;600;700&display=swap" rel="stylesheet">
<style>
  :root{
    --canvas:#0b0b0b;
    --screen:#131313;
    --screen-edge:#1b1b1b;
    --field:#1e1e1e;
    --text:#e9e9e6;
    --muted:#5c5c5c;
    --label:#bdbdbd;
    --accent:#f5a623;
    --button:#e7e7e2;
    --flag-red:#e0252b;
    --flag-white:#f4f4f4;
  }
  *{box-sizing:border-box;margin:0;padding:0}
  html,body{width:1200px;height:2215px;overflow:hidden;background:var(--canvas)}
  body{position:relative;font-family:"Montserrat",sans-serif;color:var(--text)}

  .screen{
    position:absolute;width:336px;height:var(--h,717px);
    background:linear-gradient(180deg,var(--screen) 0%,#0f0f0f 100%);
    transform-origin:top left;overflow:hidden;
    display:flex;flex-direction:column;align-items:center;
    box-shadow:0 0 0 1px var(--screen-edge);
  }
  .screen--hero{left:384px;top:30px;transform:scale(1.05)}
  .screen--compact{left:63px;top:1403px;--h:600px;transform:scale(.905)}
  .screen--edge{left:451px;top:1290px}
  .screen--classic{left:848px;top:1396px;--h:610px;transform:scale(.87)}

  .status{width:100%;display:flex;justify-content:space-between;padding:12px 18px 0;font-size:8px;color:var(--label);height:26px}
  .corner{position:absolute;top:0;right:0;width:150px;height:170px}

  .brand{margin-top:48px;align-self:flex-start;margin-left:38px;position:relative;z-index:1}
  .brand-name{font-weight:600;font-size:18px;letter-spacing:-.2px;color:var(--text)}

  .tabs{display:flex;gap:66px;margin-top:26px;font-size:12px}
  .tab{color:var(--muted);padding-bottom:8px}
  .tab--active{color:var(--text);font-weight:600;position:relative}
  .tab--active::after{content:"";position:absolute;left:50%;bottom:0;width:30px;height:2px;background:var(--text);transform:translateX(-50%)}

  .form{width:100%;margin-top:20px;padding:10px 38px 0;background:linear-gradient(180deg,#161616,#121212);display:flex;flex-direction:column;gap:8px}
  .row{display:flex;align-items:center;gap:12px;height:25px}
  .icon{width:14px;height:14px;flex:none;fill:var(--label)}
  .field{flex:1;height:25px;background:var(--field);display:flex;align-items:center;justify-content:space-between;padding:0 10px;font-size:10px;color:var(--muted)}
  .field .icon{width:12px;height:12px}
  .flag{width:18px;height:12px;flex:none;display:flex;flex-direction:column}
  .flag span{flex:1}
  .flag span:first-child{background:var(--flag-red)}
  .flag span:last-child{background:var(--flag-white)}
  .code{font-size:10px;color:var(--label);margin-left:-4px}
  .birth-label{font-size:10px;color:var(--label)}
  .date{display:flex;gap:8px}
  .date .field{justify-content:center}
  .register{margin:16px 0 14px;height:25px;background:var(--button);color:#111;font-weight:600;font-size:10px;letter-spacing:.4px;display:flex;align-items:center;justify-content:center}

  .skyline{width:100%;flex:1;min-height:40px;background:linear-gradient(180deg,#121212,#1a1a1a 70%,#111)}
  .terms{position:absolute;bottom:26px;width:100%;text-align:center;font-size:7.5px;line-height:1.5;color:var(--label)}
  .terms em{font-style:normal;color:var(--accent)}

  .device-label{position:absolute;font-size:27px;font-weight:500;color:var(--accent);transform:translateX(-50%);white-space:nowrap}

  .brand-panel{position:absolute;left:800px;top:936px;width:344px;height:281px;background:#000;display:flex;align-items:center;justify-content:center}
  .brand-panel .brand-name{font-size:44px;letter-spacing:-.5px}

  .bid{position:absolute;right:73px;top:2068px;text-align:right;font-weight:300;font-size:40px;line-height:48px;color:#dcdcdc;letter-spacing:.5px}
</style>
</head>
<body>

<svg width="0" height="0" style="position:absolute" aria-hidden="true">
  <defs>
    <linearGradient id="cornerFill" x1="0" y1="1" x2="1" y2="0">
      <stop offset="0" stop-color="#3a3a3a"/><stop offset=".6" stop-color="#8a8a8a"/><stop offset="1" stop-color="#c9c9c9"/>
    </linearGradient>
    <symbol id="i-user" viewBox="0 0 16 16"><circle cx="8" cy="5" r="3.5"/><path d="M1.5 15c0-4 3-6 6.5-6s6.5 2 6.5 6z"/></symbol>
    <symbol id="i-mail" viewBox="0 0 16 16"><path d="M1 3h14v10H1z"/><path d="M1 3l7 6 7-6v1.5L8 10.5 1 4.5z" fill="#131313"/></symbol>
    <symbol id="i-lock" viewBox="0 0 16 16"><path d="M4 7V5a4 4 0 0 1 8 0v2h1v8H3V7zm2 0h4V5a2 2 0 0 0-4 0z"/></symbol>
    <symbol id="i-eye" viewBox="0 0 16 16"><path d="M8 3C4 3 1 8 1 8s3 5 7 5 7-5 7-5-3-5-7-5zm0 8a3 3 0 1 1 0-6 3 3 0 0 1 0 6z"/><circle cx="8" cy="8" r="1.5"/></symbol>
    <symbol id="i-cal" viewBox="0 0 16 16"><path d="M2 3h12v12H2zm1.5 4v6.5h9V7z"/><rect x="4" y="1" width="2" height="3"/><rect x="10" y="1" width="2" height="3"/><rect x="5" y="8.5" width="2" height="2"/><rect x="9" y="8.5" width="2" height="2"/></symbol>
    <symbol id="i-pin" viewBox="0 0 16 16"><path d="M8 1a5 5 0 0 0-5 5c0 4 5 9 5 9s5-5 5-9a5 5 0 0 0-5-5zm0 7a2 2 0 1 1 0-4 2 2 0 0 1 0 4z"/></symbol>
  </defs>
</svg>

<section class="screen screen--hero">
  <div class="status"><span>9:41 AM</span><span></span></div>
  <svg class="corner" viewBox="0 0 150 170"><polygon points="20,0 150,0 150,170" fill="url(#cornerFill)"/><polygon points="70,0 150,0 150,95" fill="#a9a9a9" opacity=".5"/></svg>
  <div class="brand"><span class="brand-name">Keystead</span></div>
  <nav class="tabs"><span class="tab">Login</span><span class="tab tab--active">Register</span></nav>
  <form class="form">
    <div class="row"><svg class="icon"><use href="#i-user"/></svg><div class="field">Name</div></div>
    <div class="row"><svg class="icon"><use href="#i-mail"/></svg><div class="field">Email</div></div>
    <div class="row"><svg class="icon"><use href="#i-lock"/></svg><div class="field">Password<svg class="icon"><use href="#i-eye"/></svg></div></div>
    <div class="row"><div class="flag"><span></span><span></span></div><span class="code">+62</span><div class="field">Phone number</div></div>
    <div class="row"><svg class="icon"><use href="#i-cal"/></svg><span class="birth-label">Birth date</span></div>
    <div class="row date"><div class="field">DD</div><div class="field">MM</div><div class="field">YYYY</div></div>
    <div class="row"><svg class="icon"><use href="#i-pin"/></svg><div class="field">Address</div></div>
    <div class="register">REGISTER</div>
  </form>
  <div class="skyline" role="img" aria-label="Faint city skyline silhouette"></div>
  <p class="terms">By log in you agree to Keystead Member Services<br><em>Conditions of use</em> and <em>Privacy Policy</em></p>
</section>

<span class="device-label" style="left:212px;top:1268px">Compact</span>
<span class="device-label" style="left:619px;top:1200px">Edge-to-edge</span>
<span class="device-label" style="left:992px;top:1254px">Classic</span>

<section class="screen screen--compact">
  <div class="status"><span></span><span>12:30</span></div>
  <svg class="corner" viewBox="0 0 150 170"><polygon points="20,0 150,0 150,170" fill="url(#cornerFill)"/><polygon points="70,0 150,0 150,95" fill="#a9a9a9" opacity=".5"/></svg>
  <div class="brand" style="margin-top:30px"><span class="brand-name">Keystead</span></div>
  <nav class="tabs"><span class="tab">Login</span><span class="tab tab--active">Register</span></nav>
  <form class="form">
    <div class="row"><svg class="icon"><use href="#i-user"/></svg><div class="field">Name</div></div>
    <div class="row"><svg class="icon"><use href="#i-mail"/></svg><div class="field">Email</div></div>
    <div class="row"><svg class="icon"><use href="#i-lock"/></svg><div class="field">Password<svg class="icon"><use href="#i-eye"/></svg></div></div>
    <div class="row"><div class="flag"><span></span><span></span></div><span class="code">+62</span><div class="field">Phone number</div></div>
    <div class="row"><svg class="icon"><use href="#i-cal"/></svg><span class="birth-label">Birth date</span></div>
    <div class="row date"><div class="field">DD</div><div class="field">MM</div><div class="field">YYYY</div></div>
    <div class="row"><svg class="icon"><use href="#i-pin"/></svg><div class="field">Address</div></div>
    <div class="register">REGISTER</div>
  </form>
  <div class="skyline" role="img" aria-label="Faint city skyline silhouette"></div>
  <p class="terms">By log in you agree to Keystead Member Services<br><em>Conditions of use</em> and <em>Privacy Policy</em></p>
</section>

<section class="screen screen--edge">
  <div class="status"><span>9:41 AM</span><span></span></div>
  <svg class="corner" viewBox="0 0 150 170"><polygon points="20,0 150,0 150,170" fill="url(#cornerFill)"/><polygon points="70,0 150,0 150,95" fill="#a9a9a9" opacity=".5"/></svg>
  <div class="brand"><span class="brand-name">Keystead</span></div>
  <nav class="tabs"><span class="tab">Login</span><span class="tab tab--active">Register</span></nav>
  <form class="form">
    <div class="row"><svg class="icon"><use href="#i-user"/></svg><div class="field">Name</div></div>
    <div class="row"><svg class="icon"><use href="#i-mail"/></svg><div class="field">Email</div></div>
    <div class="row"><svg class="icon"><use href="#i-lock"/></svg><div class="field">Password<svg class="icon"><use href="#i-eye"/></svg></div></div>
    <div class="row"><div class="flag"><span></span><span></span></div><span class="code">+62</span><div class="field">Phone number</div></div>
    <div class="row"><svg class="icon"><use href="#i-cal"/></svg><span class="birth-label">Birth date</span></div>
    <div class="row date"><div class="field">DD</div><div class="field">MM</div><div class="field">YYYY</div></div>
    <div class="row"><svg class="icon"><use href="#i-pin"/></svg><div class="field">Address</div></div>
    <div class="register">REGISTER</div>
  </form>
  <div class="skyline" role="img" aria-label="Faint city skyline silhouette"></div>
  <p class="terms">By log in you agree to Keystead Member Services<br><em>Conditions of use</em> and <em>Privacy Policy</em></p>
</section>

<section class="screen screen--classic">
  <div class="status"><span></span><span>9:41 AM</span><span>100%</span></div>
  <svg class="corner" viewBox="0 0 150 170"><polygon points="20,0 150,0 150,170" fill="url(#cornerFill)"/><polygon points="70,0 150,0 150,95" fill="#a9a9a9" opacity=".5"/></svg>
  <div class="brand" style="margin-top:34px"><span class="brand-name">Keystead</span></div>
  <nav class="tabs"><span class="tab">Login</span><span class="tab tab--active">Register</span></nav>
  <form class="form">
    <div class="row"><svg class="icon"><use href="#i-user"/></svg><div class="field">Name</div></div>
    <div class="row"><svg class="icon"><use href="#i-mail"/></svg><div class="field">Email</div></div>
    <div class="row"><svg class="icon"><use href="#i-lock"/></svg><div class="field">Password<svg class="icon"><use href="#i-eye"/></svg></div></div>
    <div class="row"><div class="flag"><span></span><span></span></div><span class="code">+62</span><div class="field">Phone number</div></div>
    <div class="row"><svg class="icon"><use href="#i-cal"/></svg><span class="birth-label">Birth date</span></div>
    <div class="row date"><div class="field">DD</div><div class="field">MM</div><div class="field">YYYY</div></div>
    <div class="row"><svg class="icon"><use href="#i-pin"/></svg><div class="field">Address</div></div>
    <div class="register">REGISTER</div>
  </form>
  <div class="skyline" role="img" aria-label="Faint city skyline silhouette"></div>
  <p class="terms">By log in you agree to Keystead Member Services<br><em>Conditions of use</em> and <em>Privacy Policy</em></p>
</section>

<div class="brand-panel">
  <span class="brand-name">Keystead</span>
</div>

<p class="bid">35 screenshots&nbsp; for<br>$250 AUD in 1 - 2 Days</p>

</body>
</html>
```